Corporate Stationary for Beverage Alcohol Company
Brook Harbor Global Ltd. Co.
Corporate Stationary for Beverage Alcohol Company - Beverages
Creative Brief
Corporate
Dean Walter Prosser
President
512 Fenwood Drive Richmond, KY 40475
dean.prosser@brook-harbor.com
www.brook-harbor.com
The stationary shall be cutting edge and will utilize the logo art work. I would like an abstract border included on the side(s) of the letterhead, envelope and the business card.
Company Name Logo Abstract border

```html
<!DOCTYPE html>
<html lang="en">
<head>
<meta charset="utf-8">
<title>Brook Harbor Global Stationery</title>
<link href="https://fonts.googleapis.com/css2?family=Cinzel:wght@600&family=Lato:wght@400;700&display=swap" rel="stylesheet">
<style>
:root{
  --bg-edge:#3e3e3e;
  --bg-mid:#9a9a9a;
  --paper:#ffffff;
  --ink:#1a1a1a;
  --gold-dark:#a9762a;
  --gold-light:#f0d08a;
  --gold-text:#b8862e;
  --soft:#efe9dc;
  --caption:#e8e8e8;
}
*{margin:0;padding:0;box-sizing:border-box}
html,body{width:1200px;height:449px;overflow:hidden}
body{background:radial-gradient(ellipse at 50% 45%,var(--bg-mid) 0%,#6c6c6c 55%,var(--bg-edge) 100%);font-family:"Lato",Arial,sans-serif;position:relative}
.item{position:absolute;box-shadow:0 3px 8px rgba(0,0,0,.45)}
.caption{position:absolute;font-size:7px;color:var(--caption);letter-spacing:.3px}
.brand{font-family:"Cinzel",Georgia,serif;font-weight:600;color:var(--gold-text);text-align:center;line-height:1.15}
.brand-dot{display:block;width:12px;height:12px;border-radius:50%;background:var(--gold-text);margin:0 auto 3px}
svg{display:block;position:absolute;left:0;top:0}

/* business cards */
.card{width:198px;height:80px;overflow:hidden}
.card-front{left:28px;top:148px;background:var(--paper)}
.card-front .brand{position:absolute;left:10px;top:18px;width:60px;font-size:5px}
.card-front .person{position:absolute;left:100px;top:10px;font-size:6px;color:var(--ink);line-height:1.5}
.person strong{font-size:7px;color:var(--gold-text)}
.card-back-dark{left:28px;top:252px;background:#121212}
.card-back-dark .details{position:absolute;left:100px;top:40px;font-size:5px;color:#ccc;line-height:1.5}
.card-back-gold{left:28px;top:352px;background:linear-gradient(120deg,var(--gold-dark),var(--gold-light) 55%,var(--gold-dark))}
.card-back-gold .brand{position:absolute;left:0;right:0;top:26px;font-size:9px;color:var(--ink)}

/* letterheads */
.letterhead{width:223px;height:365px;top:48px;background:var(--paper);overflow:hidden}
.lh-a{left:269px}
.lh-b{left:504px}
.letterhead .brand{position:absolute;left:16px;top:16px;width:70px;font-size:5px}
.letterhead .contact{position:absolute;left:140px;top:16px;font-size:4.5px;color:#555;line-height:1.5}
.lh-b .brand{left:76px;top:14px}
.lh-b .contact{display:none}
.faint-mark{position:absolute;left:41px;top:105px;width:140px;height:140px;border-radius:50%;background:var(--soft);opacity:.7}

/* envelopes */
.envelope{width:293px;height:100px;left:888px;background:var(--paper);overflow:hidden}
.env-dark{top:112px}
.env-gold{top:218px;height:86px;background:linear-gradient(120deg,var(--gold-dark),var(--gold-light) 55%,var(--gold-dark))}
.env-white{top:312px;height:72px}
.env-wave{top:350px;left:880px;height:60px;width:300px}
.envelope .brand{position:absolute;left:0;right:0;font-size:6px}
.env-dark .brand{top:22px;color:#fff}
.env-dark .brand .brand-dot{background:#fff}
.env-gold .brand{top:24px;color:var(--ink)}
.env-gold .brand .brand-dot{background:var(--ink)}
.env-white .brand{top:8px}
.env-wave .return{position:absolute;left:10px;top:8px;font-size:4.5px;color:#555;line-height:1.5}
</style>
</head>
<body>

<!-- business card front -->
<div class="item card card-front">
  <div class="brand"><span class="brand-dot"></span>Brook Harbor Global Ltd. Co.</div>
  <div class="person"><strong>Dean Walter Prosser</strong><br>President<br>512 Fenwood Drive<br>Richmond, KY 40475<br>dean.prosser@brook-harbor.com</div>
  <svg width="198" height="80" viewBox="0 0 198 80" aria-hidden="true">
    <path d="M0 66 C60 56 130 72 198 60 L198 80 L0 80 Z" fill="var(--gold-text)"/>
    <path d="M0 63 C60 52 130 69 198 57" stroke="var(--ink)" stroke-width="2" fill="none"/>
  </svg>
</div>
<div class="caption" style="left:70px;top:232px">Front Side</div>

<!-- business card back dark -->
<div class="item card card-back-dark">
  <svg width="198" height="80" viewBox="0 0 198 80" aria-hidden="true">
    <path d="M0 70 C70 60 130 76 198 64" stroke="var(--gold-text)" stroke-width="1.5" fill="none"/>
  </svg>
  <div class="details">www.brook-harbor.com</div>
</div>
<div class="caption" style="left:70px;top:336px">Back Side</div>

<!-- business card back gold -->
<div class="item card card-back-gold">
  <div class="brand">Brook Harbor Global</div>
</div>
<div class="caption" style="left:70px;top:436px">Back Option</div>

<!-- letterhead A -->
<div class="item letterhead lh-a">
  <div class="brand"><span class="brand-dot"></span>Brook Harbor Global Ltd. Co.</div>
  <div class="contact">512 Fenwood Drive<br>Richmond, KY 40475<br>www.brook-harbor.com</div>
  <div class="faint-mark" role="img" aria-label="Faint brand emblem watermark"></div>
  <svg width="223" height="365" viewBox="0 0 223 365" aria-hidden="true">
    <defs><linearGradient id="goldA" x1="0" x2="1"><stop offset="0" stop-color="#a9762a"/><stop offset=".55" stop-color="#f0d08a"/><stop offset="1" stop-color="#a9762a"/></linearGradient></defs>
    <path d="M0 330 C70 312 150 340 223 318 L223 365 L0 365 Z" fill="url(#goldA)"/>
    <path d="M0 325 C70 306 150 334 223 312" stroke="var(--ink)" stroke-width="3" fill="none"/>
  </svg>
</div>
<div class="caption" style="left:345px;top:420px">Letterhead Option A</div>

<!-- letterhead B -->
<div class="item letterhead lh-b">
  <div class="brand"><span class="brand-dot"></span>Brook Harbor Global Ltd. Co.</div>
  <div class="faint-mark" role="img" aria-label="Faint brand emblem watermark"></div>
  <svg width="223" height="365" viewBox="0 0 223 365" aria-hidden="true">
    <defs><linearGradient id="goldB" x1="0" x2="1"><stop offset="0" stop-color="#a9762a"/><stop offset=".55" stop-color="#f0d08a"/><stop offset="1" stop-color="#a9762a"/></linearGradient></defs>
    <path d="M0 318 C80 340 150 310 223 332 L223 365 L0 365 Z" fill="url(#goldB)"/>
    <path d="M0 312 C80 334 150 304 223 326" stroke="var(--ink)" stroke-width="3" fill="none"/>
  </svg>
</div>
<div class="caption" style="left:580px;top:420px">Letterhead Option B</div>

<!-- envelopes -->
<div class="item envelope env-dark">
  <svg width="293" height="100" viewBox="0 0 293 100" aria-hidden="true">
    <path d="M0 0 H293 V30 L146 62 L0 30 Z" fill="#141414"/>
  </svg>
  <div class="brand"><span class="brand-dot"></span>Brook Harbor</div>
</div>
<div class="item envelope env-gold">
  <div class="brand"><span class="brand-dot"></span>Brook Harbor</div>
</div>
<div class="item envelope env-white">
  <div class="brand"><span class="brand-dot"></span>Brook Harbor</div>
  <svg width="293" height="72" viewBox="0 0 293 72" aria-hidden="true">
    <path d="M0 0 L146 40 L293 0" stroke="#ddd" stroke-width="1" fill="none"/>
  </svg>
</div>
<div class="item envelope env-wave">
  <div class="return">Brook Harbor Global Ltd. Co.<br>512 Fenwood Drive, Richmond, KY 40475</div>
  <svg width="300" height="60" viewBox="0 0 300 60" aria-hidden="true">
    <path d="M0 50 C90 40 200 58 300 44 L300 60 L0 60 Z" fill="var(--gold-text)"/>
    <path d="M0 47 C90 36 200 55 300 41" stroke="var(--ink)" stroke-width="2" fill="none"/>
  </svg>
</div>
<div class="caption" style="left:1000px;top:418px">Envelope Designs</div>

</body>
</html>
```